Website for Bramblewood Quarry Advisors

Please design a website that initially contains four or five pages. This work is for a newly formed consulting company, Bramblewood Quarry Advisors, that provides training and individual coaching to help business professionals and lawyers write more effectively and efficiently.

We work in a professional and conservative industry. The website should be simple, crisp, and clean.

I have attached a document that describes the four initial pages for the site: 1) a landing page, 2) a webpage that includes the pictures and bios of our two consultants, 3) a webpage that describes our services, and 4) a webpage that will contain a form that visitors can use to submit questions to us.

I also included the following files:
a. a powerpoint slide with our consultants' pictures and bios; and
b. our recently designed logo (jpg and png files).

Thank you!

```html
<!DOCTYPE html>
<html lang="en">
<head>
<meta charset="utf-8">
<title>Bramblewood Quarry Advisors</title>
<link href="https://fonts.googleapis.com/css2?family=Open+Sans:wght@400;600;700&display=swap" rel="stylesheet">
<style>
:root{
  --red:#c3242b;
  --red-dark:#8e1419;
  --ink:#1f1f1f;
  --dark:#222222;
  --footer:#24262b;
  --paper:#f5f5f5;
  --white:#ffffff;
  --muted:#8a8a8a;
  --line:#e6e6e6;
  --star:#f05a28;
}
*{box-sizing:border-box;margin:0;padding:0}
html,body{width:1200px;height:4615px;overflow:hidden}
body{position:relative;background:var(--paper);font-family:"Open Sans",Arial,sans-serif;color:var(--ink)}
.abs{position:absolute}
a{color:inherit}

/* header */
.site-header{left:0;top:0;width:1200px;height:80px;background:var(--white)}
.brand{left:107px;top:34px;font-size:14px;font-weight:600;color:var(--ink);display:flex;align-items:center;gap:8px;white-space:nowrap}
.brand-mark{width:8px;height:8px;background:var(--red)}
.main-nav{left:400px;top:50px;font-size:11px;color:#555}
.main-nav span{position:absolute;white-space:nowrap}
.main-nav .active{color:var(--ink);font-weight:700}
.top-tab{left:842px;top:0;width:111px;height:22px;background:#6a6f78;color:#fff;font-size:9px;font-weight:600;text-align:center;line-height:20px;letter-spacing:.5px}

/* hero */
.hero{left:0;top:80px;width:1200px;height:760px;overflow:hidden}
.hero-photo{position:absolute;left:0;top:0;width:1200px;height:630px;background:linear-gradient(110deg,#1e2a33 0%,#2d3b45 35%,#4a5660 60%,#2a333a 100%)}
.hero-band{position:absolute;left:0;top:630px;width:1200px;height:130px;background:linear-gradient(180deg,#2a333a 0%,#8e1419 30%,#c3242b 50%,#f5f5f5 100%)}
.hero-eyebrow{left:109px;top:188px;color:#fff;font-size:12px;letter-spacing:.4px;display:flex;align-items:center;gap:14px;white-space:nowrap}
.hero-eyebrow::after{content:"";width:44px;height:1px;background:#fff}
.hero-title{left:109px;top:242px;color:#fff;font-size:42px;line-height:57px;font-weight:700;white-space:nowrap}
.hero-text{left:109px;top:395px;width:410px;color:#fff;font-size:13px;line-height:22px}
.btn{display:flex;align-items:center;justify-content:center;background:var(--red);color:#fff;font-weight:700;font-size:13px;border-radius:3px;white-space:nowrap}
.hero .btn{left:109px;top:475px;width:169px;height:47px}

/* section heads */
.section-title{left:0;width:1200px;text-align:center;font-size:29px;font-weight:700;color:var(--ink)}
.section-sub{left:330px;width:540px;text-align:center;font-size:12.5px;line-height:22px;color:var(--muted)}

/* why cards */
.why-card{top:969px;width:235px;height:217px;background:var(--white);box-shadow:0 2px 10px rgba(0,0,0,.09);text-align:center;border-radius:3px}
.why-card svg{margin-top:34px}
.why-card h3{font-size:18px;line-height:25px;font-weight:700;margin-top:10px}
.why-card p{font-size:12.5px;line-height:22px;color:var(--muted);margin-top:8px;padding:0 20px}
.why-card.featured{background:var(--dark);color:#fff}
.why-card.featured p{color:#ddd}
.why-more{left:523px;top:1225px;width:168px;height:45px}

/* message */
.message-band{left:281px;top:1318px;width:919px;height:469px;background:var(--dark)}
.message-photo{left:0;top:1386px;width:582px;height:446px;background:linear-gradient(135deg,#6d7783 0%,#a9b0b6 45%,#3a3f45 100%)}
.message-title{left:632px;top:1408px;color:#fff;font-size:29px;font-weight:700;white-space:nowrap}
.message-text{left:630px;top:1462px;width:430px;color:#fff;font-size:13px;line-height:21.5px}
.message-text p+p{margin-top:10px}
.message-btn{left:630px;top:1651px;width:156px;height:43px;gap:10px}

/* services */
.service-photo{top:2061px;width:320px;height:237px}
.service-card{top:2239px;width:286px;height:200px;background:var(--white);box-shadow:0 2px 10px rgba(0,0,0,.08);padding:24px 40px 0 40px}
.service-card h3{font-size:21px;font-weight:700;white-space:nowrap}
.service-card p{font-size:12.5px;line-height:21.5px;color:var(--muted);margin-top:8px}
.service-card .more{display:block;margin-top:10px;font-size:11px;font-weight:700;color:var(--red)}
.service-card.featured{background:var(--dark);color:#fff}
.service-card.featured p{color:#ddd}
.service-card.featured .more{color:#fff}

/* call to action */
.cta{left:0;top:2511px;width:1200px;height:294px;background:linear-gradient(90deg,#2f3a44 0%,#55606a 50%,#2f3a44 100%)}
.cta-phone{left:0;top:2561px;width:1200px;text-align:center;color:#fff;font-size:22px;font-weight:600}
.cta-title{left:0;top:2601px;width:1200px;text-align:center;color:#fff;font-size:30px;font-weight:700}
.cta-text{left:330px;top:2659px;width:540px;text-align:center;color:#fff;font-size:12.5px;line-height:22px}
.cta-btn{left:519px;top:2719px;width:167px;height:45px;border:1.5px solid #fff;border-radius:4px;color:#fff;font-weight:700;font-size:13px;display:flex;align-items:center;justify-content:center}

/* reviews */
.review{top:3012px;width:494px;height:257px;background:#ececec}
.review-rule{position:absolute;left:62px;top:42px;width:1px;height:175px;background:#555}
.review-quote{position:absolute;left:38px;top:106px;width:50px;height:50px;border-radius:50%;background:#fff;border:2px solid var(--red);display:flex;align-items:center;justify-content:center}
.review-quote span{width:38px;height:38px;border-radius:50%;background:var(--red);display:flex;align-items:center;justify-content:center}
.stars{position:absolute;left:113px;top:40px;color:var(--star);font-size:16px;letter-spacing:3px}
.review-text{position:absolute;left:113px;top:84px;width:340px;font-size:12.5px;line-height:22px;color:var(--muted)}
.review-name{position:absolute;left:113px;top:172px;font-size:16px;font-weight:700}
.review-place{position:absolute;left:113px;top:198px;font-size:12px;color:#555}
.review-avatar{position:absolute;left:400px;top:164px;width:58px;height:58px;border-radius:50%;background:linear-gradient(135deg,#d9c1a8,#8a7766)}
.dots{left:565px;top:3311px;display:flex;gap:8px}
.dots i{width:10px;height:10px;border-radius:50%;background:var(--star);display:block}
.dots i.off{background:none;border:1.5px solid var(--star)}

/* contact */
.contact-band{left:0;top:3362px;width:1200px;height:802px;background:#f0f0f0}
.contact-panel{left:90px;top:3568px;width:510px;height:462px;background:linear-gradient(120deg,#2b2b2b 0%,#4a4039 55%,#2e2a27 100%);color:#fff}
.contact-panel .inner{position:absolute;left:86px;top:66px;font-size:12px;line-height:19px;font-weight:600;white-space:nowrap}
.contact-panel h4{font-size:16px;font-weight:700;margin-bottom:18px}
.contact-panel .call{font-size:19px;font-weight:700;margin-bottom:4px}
.contact-panel .gap{height:24px}
.socials{position:absolute;left:86px;top:371px;display:flex;gap:10px}
.socials i{width:32px;height:32px;border-radius:50%;background:#8c8c8c;display:block}
.socials i.on{background:#fff}
.contact-form{left:600px;top:3568px;width:507px;height:462px;background:var(--white)}
.form-title{position:absolute;left:87px;top:63px;color:#1f3a8a;font-size:16px;font-weight:700}
.field{position:absolute;left:87px;width:333px;height:30px;background:#f3f3f3;font-size:10px;color:#666;padding:8px 14px}
.field.message{height:95px}
.submit{position:absolute;left:87px;top:371px;width:110px;height:37px;font-size:12px}

/* info bar */
.info-bar{left:66px;top:4112px;width:1069px;height:104px;background:var(--red);border-radius:6px;color:#fff;z-index:2}
.info-item{position:absolute;top:36px;white-space:nowrap}
.info-item h5{font-size:17px;font-weight:700}
.info-item p{font-size:13px;margin-top:6px}
.info-icon{position:absolute;top:26px}
.info-sep{position:absolute;top:0}

/* footer */
.site-footer{left:0;top:4164px;width:1200px;height:451px;background:var(--footer);color:#fff}
.footer-col{top:4286px;color:#fff}
.footer-col h5{font-size:18px;font-weight:700;white-space:nowrap}
.footer-col h5::after{content:"";display:block;width:36px;height:2px;background:var(--red);margin-top:12px}
.footer-about{left:66px;width:320px;font-size:13px;line-height:32px;color:#fff}
.footer-about a{color:#2aa9e0;font-size:16px}
.link-list{position:absolute;top:66px;font-size:13px;line-height:33px;white-space:nowrap}
.link-list a{display:block;text-decoration:underline}
.subscribe-text{font-size:14px;line-height:24px;margin-top:24px;width:340px}
.subscribe{position:absolute;left:0;top:132px;width:338px;height:54px;background:#fff;border-radius:4px;overflow:hidden}
.subscribe span{position:absolute;left:18px;top:17px;color:#555;font-size:13px}
.subscribe b{position:absolute;right:0;top:0;width:64px;height:54px;background:var(--red);display:flex;align-items:center;justify-content:center}
.footer-bottom{left:0;top:4549px;width:1200px;height:1px;background:#3a3c42}
.footer-brand{left:66px;top:4549px;width:172px;height:66px;background:var(--red);color:#fff;font-size:9px;font-weight:600;display:flex;align-items:center;justify-content:center;white-space:nowrap}
.footer-social{top:4549px;width:58px;height:66px;border-left:1px solid #3a3c42;display:flex;align-items:center;justify-content:center}
.footer-social i{width:12px;height:12px;border-radius:50%;background:#6e7077;display:block}
</style>
</head>
<body>

<header class="abs site-header">
  <div class="abs brand"><span class="brand-mark"></span>Bramblewood Quarry Advisors</div>
  <nav class="abs main-nav">
    <span class="active" style="left:0">Home</span>
    <span style="left:84px">About Us</span>
    <span style="left:184px">Services</span>
    <span style="left:283px">Our Team</span>
    <span style="left:396px">Projects</span>
    <span style="left:483px">Contact Us</span>
  </nav>
  <div class="abs top-tab">BOOK A CALL</div>
</header>

<section class="abs hero">
  <div class="hero-photo" role="img" aria-label="Team of consultants meeting around a boardroom table"></div>
  <div class="hero-band" role="img" aria-label="Decorative red wave dividing the hero from the page"></div>
  <div class="abs hero-eyebrow">WRITING CONSULTANTS</div>
  <h1 class="abs hero-title">Words That Speak,<br>Strategies That Succeed</h1>
  <p class="abs hero-text">Lorem ipsum dolor sit amet, consectetur adipiscing elit, sed d o eiusmod temp dipiscing elit, sed d</p>
  <div class="abs btn">Contact Us</div>
</section>

<h2 class="abs section-title" style="top:838px">Why we are the best</h2>
<p class="abs section-sub" style="top:893px">Lorem ipsum dolor sit amet, consectetur adipiscing elit, sed do eiusmod tempor incididunt ut labore et dolore magna aliqua. Ut enim ad min</p>

<div class="abs why-card" style="left:91px">
  <svg width="40" height="40" viewBox="0 0 40 40" fill="none" stroke="#c3242b" stroke-width="2"><path d="M20 6 L33 16 L28 32 L12 32 L7 16 Z"/><circle cx="20" cy="6" r="2.5"/><circle cx="33" cy="16" r="2.5"/><circle cx="7" cy="16" r="2.5"/></svg>
  <h3>Personalized<br>Approach</h3>
  <p>Lorem ipsum dolor sit amet, consectetur adipiscing</p>
</div>
<div class="abs why-card featured" style="left:351px">
  <svg width="40" height="40" viewBox="0 0 40 40" fill="none" stroke="#c3242b" stroke-width="2"><path d="M6 34 H34"/><path d="M10 30 L16 10 L26 16 L20 30 Z"/><circle cx="20" cy="20" r="2"/></svg>
  <h3>Proven<br>Track Record</h3>
  <p>Lorem ipsum dolor sit amet, consectetur adipiscing</p>
</div>
<div class="abs why-card" style="left:611px">
  <svg width="40" height="40" viewBox="0 0 40 40" fill="none" stroke="#c3242b" stroke-width="2"><path d="M8 30 A14 14 0 1 1 32 30"/><path d="M20 22 L20 13"/><circle cx="20" cy="24" r="2"/></svg>
  <h3>Empathetic<br>Staff</h3>
  <p>Lorem ipsum dolor sit amet, consectetur adipiscing</p>
</div>
<div class="abs why-card" style="left:870px">
  <svg width="40" height="40" viewBox="0 0 40 40" fill="none" stroke="#c3242b" stroke-width="2"><circle cx="20" cy="13" r="6"/><path d="M8 33 C8 24 32 24 32 33 Z"/></svg>
  <h3>Client<br>Centric</h3>
  <p>Lorem ipsum dolor sit amet, consectetur adipiscing</p>
</div>
<div class="abs btn why-more">Learn More</div>

<div class="abs message-band"></div>
<div class="abs message-photo" role="img" aria-label="Two colleagues reviewing a tablet together in an office"></div>
<h2 class="abs message-title">Every Message Matters</h2>
<div class="abs message-text">
  <p>Lorem ipsum dolor sit amet, consectetur adipiscing elit, sed do eiusmod tempor &nbsp;incididunt ut labore et dolore magna aliqua. Ut e nim ad min veniam, quis nostrud ex.</p>
  <p>Lorem ipsum dolor sit amet, consectetur adipiscing elit, sed do eiusmod tempor &nbsp;incididunt ut labore et dolore magna aliqua. Ut e nim ad min veniam, quis nostrud ex. et dolore magna aliqua. Ut e nim ad min veniam, quis nostrud ex.</p>
</div>
<div class="abs btn message-btn">Learn More
  <svg width="18" height="14" viewBox="0 0 18 14" fill="none" stroke="#fff" stroke-width="2"><path d="M1 7 H16 M10 1 L16 7 L10 13"/></svg>
</div>

<h2 class="abs section-title" style="top:1907px">Our Services</h2>
<p class="abs section-sub" style="top:1963px">Lorem ipsum dolor sit amet, consectetur adipiscing elit, sed do eiusmod tempor incididunt ut labore et dolore magna aliqua. Ut enim ad min</p>

<div class="abs service-photo" style="left:93px;background:linear-gradient(135deg,#4a5a6a,#9aa4ad)" role="img" aria-label="Colleagues discussing strategy at a laptop"></div>
<div class="abs service-photo" style="left:439px;background:linear-gradient(135deg,#3b4148,#8b9096)" role="img" aria-label="Consultant holding a tablet in a modern office"></div>
<div class="abs service-photo" style="left:786px;background:linear-gradient(135deg,#b6a594,#6a5e55)" role="img" aria-label="Group of colleagues working together on content"></div>

<div class="abs service-card" style="left:109px">
  <h3>Strategy</h3>
  <p>Lorem ipsum dolor sit amet, cons ectetur adipiscing elit, sed do eiu smod tempor incididunt ut labore et dolore magna aliqua.</p>
  <span class="more">LEARN MORE</span>
</div>
<div class="abs service-card featured" style="left:458px">
  <h3>Technical Writing</h3>
  <p>Lorem ipsum dolor sit amet, cons ectetur adipiscing elit, sed do eiu smod tempor incididunt ut labore et dolore magna aliqua.</p>
  <span class="more">LEARN MORE</span>
</div>
<div class="abs service-card" style="left:804px">
  <h3>Content Creation</h3>
  <p>Lorem ipsum dolor sit amet, cons ectetur adipiscing elit, sed do eiu smod tempor incididunt ut labore et dolore magna aliqua.</p>
  <span class="more">LEARN MORE</span>
</div>

<section class="abs cta" role="img" aria-label="Smiling professionals in a bright office, darkened behind text"></section>
<div class="abs cta-phone">147-220-5830</div>
<h2 class="abs cta-title">Eloquent Expression, Profound Impression.</h2>
<p class="abs cta-text">Lorem ipsum dolor sit amet, consectetur adipiscing elit, sed do eiusmod tempor incididunt ut labore et dolore magna aliqua. Ut enim ad min</p>
<div class="abs cta-btn">Contact Us</div>

<h2 class="abs section-title" style="top:2862px">Client Reviews</h2>
<p class="abs section-sub" style="top:2918px">Lorem ipsum dolor sit amet, consectetur adipiscing elit, sed do eiusmod tempor incididunt ut labore et dolore magna aliqua. Ut enim ad min</p>

<div class="abs review" style="left:90px">
  <div class="review-rule"></div>
  <div class="review-quote"><span><svg width="18" height="14" viewBox="0 0 18 14" fill="#fff"><path d="M1 1 H7 V7 L4 13 H1 L3 7 H1 Z M10 1 H16 V7 L13 13 H10 L12 7 H10 Z"/></svg></span></div>
  <div class="stars">★★★★★</div>
  <p class="review-text">Lorem ipsum dolor sit amet, consectetur adipiscing elit, sed do eiusmod tempor incididunt ut labore et d olore magna aliqua.</p>
  <div class="review-name">Maren Holt</div>
  <div class="review-place">Green Valley</div>
  <div class="review-avatar" role="img" aria-label="Reviewer portrait"></div>
</div>
<div class="abs review" style="left:609px">
  <div class="review-rule"></div>
  <div class="review-quote"><span><svg width="18" height="14" viewBox="0 0 18 14" fill="#fff"><path d="M1 1 H7 V7 L4 13 H1 L3 7 H1 Z M10 1 H16 V7 L13 13 H10 L12 7 H10 Z"/></svg></span></div>
  <div class="stars">★★★★★</div>
  <p class="review-text">Lorem ipsum dolor sit amet, consectetur adipiscing elit, sed do eiusmod tempor incididunt ut labore et d olore magna aliqua.</p>
  <div class="review-name">Maren Holt</div>
  <div class="review-place">Green Valley</div>
  <div class="review-avatar" role="img" aria-label="Reviewer portrait"></div>
</div>
<div class="abs dots"><i></i><i></i><i class="off"></i><i></i></div>

<section class="abs contact-band"></section>
<h2 class="abs section-title" style="top:3417px">Feel free to contact us</h2>
<p class="abs section-sub" style="top:3473px">Lorem ipsum dolor sit amet, consectetur adipiscing elit, sed do eiusmod tempor incididunt ut labore et dolore magna aliqua. Ut enim ad min</p>

<div class="abs contact-panel" role="img" aria-label="Smiling consultant in an office, darkened behind contact details">
  <div class="inner">
    <h4>CONTACT US</h4>
    <div class="call">Call: 0147 220 583</div>
    <div>hello@bramblewoodquarry.com</div>
    <div class="gap"></div>
    <div>Address:<br>SOME PLACE<br>51100 Road</div>
    <div class="gap"></div>
    <div>Operating Hours<br>Monday to Saturday: 9:00 - 18:00<br>Sunday: Closed</div>
  </div>
  <div class="socials"><i></i><i class="on"></i><i></i><i></i></div>
</div>
<div class="abs contact-form">
  <div class="form-title">FREE CONSULTATION</div>
  <div class="field" style="top:116px">Your Name</div>
  <div class="field" style="top:165px">Email</div>
  <div class="field" style="top:214px">Phone</div>
  <div class="field message" style="top:263px">Message</div>
  <div class="btn submit">SUBMIT</div>
</div>

<footer class="abs site-footer"></footer>

<div class="abs info-bar">
  <svg class="info-icon" style="left:46px" width="56" height="50" viewBox="0 0 56 50" fill="none" stroke="#fff" stroke-width="2"><path d="M28 4 C20 4 15 10 15 17 C15 27 28 38 28 38 C28 38 41 27 41 17 C41 10 36 4 28 4 Z"/><circle cx="28" cy="17" r="5"/><path d="M12 32 L3 46 H53 L44 32"/></svg>
  <div class="info-item" style="left:108px"><h5>Location</h5><p>123, City, Country</p></div>
  <svg class="info-sep" style="left:346px" width="24" height="104" viewBox="0 0 24 104" fill="none" stroke="#fff" stroke-width="1.5" opacity=".8"><path d="M2 0 L22 52 L2 104"/></svg>
  <svg class="info-icon" style="left:402px" width="50" height="50" viewBox="0 0 50 50" fill="none" stroke="#fff" stroke-width="2"><rect x="8" y="4" width="22" height="42" rx="3"/><path d="M15 40 H23"/><path d="M36 18 Q40 25 36 32 M41 14 Q47 25 41 36"/></svg>
  <div class="info-item" style="left:466px"><h5>Telephone</h5><p>+147 220 58301</p></div>
  <svg class="info-sep" style="left:701px" width="24" height="104" viewBox="0 0 24 104" fill="none" stroke="#fff" stroke-width="1.5" opacity=".8"><path d="M2 0 L22 52 L2 104"/></svg>
  <svg class="info-icon" style="left:755px" width="54" height="50" viewBox="0 0 54 50" fill="none" stroke="#fff" stroke-width="2"><rect x="4" y="14" width="46" height="32" rx="2"/><path d="M4 16 L27 34 L50 16"/><path d="M14 14 V4 H40 V14"/></svg>
  <div class="info-item" style="left:822px"><h5>Email</h5><p>hello@bramblewoodquarry.com</p></div>
</div>

<div class="abs footer-col" style="left:66px">
  <h5>About Company</h5>
</div>
<p class="abs footer-about" style="top:4354px">Lorem ipsum dolor sit amet, consectetur adipis cing elit, sed do eiusmod tempor incididunt ut labore et dolore magna aliqua.<br><a>Read More</a></p>

<div class="abs footer-col" style="left:433px">
  <h5>Useful Links</h5>
  <div class="link-list" style="left:0"><a>About Us</a><a>Projects</a><a>Blog</a><a>Contact Us</a></div>
  <div class="link-list" style="left:177px"><a>Services</a><a>Shop</a><a>Privacy Policy</a><a>Help Desk</a></div>
</div>

<div class="abs footer-col" style="left:797px">
  <h5>Subscribe</h5>
  <p class="subscribe-text">If you have any questions, Subscribe to our newsletter to know more</p>
  <div class="subscribe"><span>Email</span><b><svg width="12" height="18" viewBox="0 0 12 18" fill="none" stroke="#fff" stroke-width="2.5"><path d="M2 2 L10 9 L2 16"/></svg></b></div>
</div>

<div class="abs footer-bottom"></div>
<div class="abs footer-brand">Bramblewood Quarry Advisors</div>
<div class="abs footer-social" style="left:902px"><i></i></div>
<div class="abs footer-social" style="left:960px"><i></i></div>
<div class="abs footer-social" style="left:1018px"><i></i></div>
<div class="abs footer-social" style="left:1076px"><i></i></div>

</body>
</html>
```